The Leadership Horizon Business Card

We need an attractive business card with the logo that we bought from ArtQuarry last year.
Our mission is to contribute to change the way today's leaders manage business companies bringing value to the workplace and helping them to build a new model of creating wealth.
Our logo is clear about our values : we seek Positive Change through People and are convinced that the pursuit of individual well-being and the chase of economic results can converge with the right management.
Industry/Entity Type
Management Consulting
Contact Information for Business Card
Corinne Valbrec
+34 612 80 27 35
corinne.valbrec@leadershiphorizonexample.com
www.leadershiphorizonexample.com
Look and feel
Each slider illustrates characteristics of the customer's brand and the style your logo design should communicate.

```html
<!DOCTYPE html>
<html lang="en">
<head>
<meta charset="utf-8">
<title>The Leadership Horizon Business Card</title>
<link rel="stylesheet" href="https://fonts.googleapis.com/css2?family=Cinzel:wght@500;600&family=Open+Sans:wght@400;600&display=swap">
<style>
  :root {
    --stage-top: #3e3e3e;
    --stage-bottom: #4a4a4a;
    --card-white: #ffffff;
    --brand-teal: #1d7b79;
    --back-teal: #08a890;
    --text-dark: #2e2e2e;
    --rule-teal: #3a9c97;
    --light: #ffffff;
  }
  * { box-sizing: border-box; margin: 0; padding: 0; }
  html, body { width: 1200px; height: 900px; overflow: hidden; }
  body {
    background: linear-gradient(180deg, var(--stage-top), var(--stage-bottom));
    position: relative;
    font-family: "Open Sans", Arial, sans-serif;
  }
  .card {
    position: absolute;
    top: 306px;
    width: 440px;
    height: 271px;
    border-radius: 10px;
    box-shadow: 0 2px 6px rgba(0,0,0,0.35);
    overflow: hidden;
  }
  .card-front { left: 149px; background: var(--card-white); }
  .card-back { left: 608px; background: var(--back-teal); }

  .brand-block {
    position: absolute;
    left: 162px; top: 30px;
    width: 254px;
    display: flex;
    flex-direction: column;
    align-items: center;
  }
  .brand-mark {
    width: 54px; height: 54px;
    border-radius: 50%;
    background: var(--brand-teal);
  }
  .brand-name {
    margin-top: 20px;
    width: 100%;
    text-align: center;
    font-family: "Cinzel", Georgia, serif;
    font-weight: 600;
    color: var(--brand-teal);
    line-height: 1;
  }
  .brand-name .line-1 { display: block; font-size: 26px; white-space: nowrap; }
  .brand-name .line-2 {
    display: flex; align-items: center; gap: 8px;
    font-size: 12px; letter-spacing: 5px; margin-top: 5px;
    font-weight: 500;
  }
  .brand-name .line-2::before,
  .brand-name .line-2::after {
    content: ""; flex: 1; height: 1px; background: var(--rule-teal);
  }

  .holder {
    position: absolute;
    left: 24px; top: 169px;
    right: 23px;
    display: flex;
    align-items: center;
    gap: 8px;
  }
  .holder-name {
    font-family: "Cinzel", Georgia, serif;
    font-weight: 600;
    font-size: 18px;
    color: var(--brand-teal);
    white-space: nowrap;
  }
  .holder-rule { flex: 1; height: 1px; background: var(--rule-teal); margin-top: 2px; }

  .contacts {
    position: absolute;
    right: 23px; top: 202px;
    list-style: none;
    text-align: right;
    font-size: 12.2px;
    color: var(--text-dark);
    line-height: 16px;
  }
  .contacts li { display: flex; justify-content: flex-end; align-items: center; gap: 6px; white-space: nowrap; }
  .contacts svg { width: 9px; height: 9px; fill: var(--brand-teal); }

  .back-mark {
    position: absolute;
    left: 190px; top: 70px;
    width: 60px; height: 60px;
    border-radius: 50%;
    background: var(--light);
  }
  .back-name {
    position: absolute;
    left: 0; right: 0; top: 146px;
    text-align: center;
    font-family: "Cinzel", Georgia, serif;
    font-weight: 600;
    font-size: 24px;
    color: var(--light);
  }
  .back-url {
    position: absolute;
    left: 0; right: 0; top: 231px;
    text-align: center;
    font-size: 12px;
    font-weight: 600;
    color: var(--light);
  }
</style>
</head>
<body>
  <section class="card card-front">
    <div class="brand-block">
      <div class="brand-mark" aria-hidden="true"></div>
      <h1 class="brand-name"><span class="line-1">The Leadership</span><span class="line-2">Horizon</span></h1>
    </div>
    <div class="holder">
      <h2 class="holder-name">Corinne Valbrec</h2>
      <span class="holder-rule"></span>
    </div>
    <ul class="contacts">
      <li>+34 612 80 27 35
        <svg viewBox="0 0 10 10" aria-hidden="true"><path d="M2 0.5l1.6 0 0.6 2.2-1 0.8c0.5 1.2 1.3 2 2.5 2.5l0.8-1 2.2 0.6 0 1.6c0 0.6-0.5 1-1 1C3.8 8.2 1.8 6.2 1 2.5 1 1 1.4 0.5 2 0.5z"/></svg>
      </li>
      <li>www.leadershiphorizonexample.com
        <svg viewBox="0 0 10 10" aria-hidden="true"><circle cx="5" cy="5" r="4.5"/></svg>
      </li>
      <li>corinne.valbrec@leadershiphorizonexample.com
        <svg viewBox="0 0 10 10" aria-hidden="true"><path d="M0.5 2h9v6h-9z M0.5 2l4.5 3.5 4.5-3.5" stroke="#fff" stroke-width="0.8"/></svg>
      </li>
    </ul>
  </section>

  <section class="card card-back">
    <div class="back-mark" aria-hidden="true"></div>
    <p class="back-name">The Leadership Horizon</p>
    <p class="back-url">www.leadershiphorizonexample.com</p>
  </section>
</body>
</html>
```